Speisekarten
Zielgruppe
we run a restaurant and our target groups are families and business people
Aufgabenstellung
The menu consists of a black folder with 8 DIN A4 slots which have a 2 cm border on all sides. The card should be discreet, classy and easy to read without any kind of complicated fonts or pictures. we would like to see creative designs regarding our recommendation at the end of page 3.

```html
<!DOCTYPE html>
<html lang="de">
<head>
<meta charset="utf-8">
<title>NOVAN – Aperitif</title>
<link rel="stylesheet" href="https://fonts.googleapis.com/css2?family=Poppins:wght@500;600&display=swap">
<style>
  :root {
    --paper: #ffffff;
    --ink: #000000;
    --gold: #d39c52;
    --white: #ffffff;
    --rule: #9a9a9a;
    --frame: #d8d8d8;
  }
  * { margin: 0; padding: 0; box-sizing: border-box; }
  html, body { width: 849px; height: 1200px; overflow: hidden; background: var(--paper); }
  .menu-page {
    position: relative;
    width: 849px; height: 1200px;
    background: var(--paper);
    font-family: "Poppins", sans-serif;
  }
  .menu-sheet {
    position: absolute;
    left: 11px; top: 11px; right: 10px; bottom: 8px;
    background: var(--ink);
  }
  .brand-name {
    position: absolute;
    left: 0; right: 0; top: 180px;
    text-align: center;
    color: var(--gold);
    font-weight: 500;
    font-size: 64px;
    letter-spacing: 2px;
    line-height: 1;
  }
  .section-frame {
    position: absolute;
    left: 70px; top: 324px;
    width: 687px; height: 785px;
    border: 1px solid var(--frame);
  }
  .section-title {
    position: absolute;
    left: 334px; top: 300px;
    width: 162px; height: 47px;
    background: var(--ink);
    border: 1px solid var(--frame);
    color: var(--gold);
    font-weight: 600;
    font-size: 20px;
    display: flex; align-items: center; justify-content: center;
    letter-spacing: 0.5px;
  }
  .drink-list { list-style: none; }
  .drink {
    position: absolute;
    left: 107px; width: 611px;
    display: flex; align-items: flex-end;
    font-size: 12.5px; font-weight: 500;
    line-height: 1.6;
  }
  .drink-name { color: var(--gold); min-width: 160px; white-space: nowrap; }
  .drink-name.is-tight { min-width: 0; margin-right: 6px; }
  .leader {
    flex: 1;
    border-bottom: 1px solid var(--rule);
    margin: 0 8px 6px 0;
  }
  .leader.is-short { flex: none; width: 22px; margin: 0 6px 6px 6px; }
  .leader.is-price { flex: none; width: 58px; margin: 0 4px 6px 8px; }
  .volume, .price { color: var(--white); font-weight: 600; white-space: nowrap; }
  .volume { min-width: 34px; text-align: right; }
  .price { width: 40px; text-align: right; }
</style>
</head>
<body>
<main class="menu-page">
  <div class="menu-sheet">
    <h1 class="brand-name">NOVAN</h1>
  </div>

  <section class="section-frame" aria-labelledby="aperitif-title"></section>
  <h2 class="section-title" id="aperitif-title">APERITIF</h2>

  <ul class="drink-list">
    <li class="drink" style="top:400px"><span class="drink-name">VELOUR WILD BERRY</span><span class="leader"></span><span class="volume">0,2L</span><span class="leader is-price"></span><span class="price">9,00</span></li>
    <li class="drink" style="top:445px"><span class="drink-name">HUGO</span><span class="leader"></span><span class="volume">0,2L</span><span class="leader is-price"></span><span class="price">8,50</span></li>
    <li class="drink" style="top:490px"><span class="drink-name">ARANZO SPRITZ</span><span class="leader"></span><span class="volume">0,2L</span><span class="leader is-price"></span><span class="price">8,50</span></li>
    <li class="drink" style="top:534px"><span class="drink-name">SEKT ARANZO</span><span class="leader"></span><span class="volume">0,1L</span><span class="leader is-price"></span><span class="price">8,00</span></li>
    <li class="drink" style="top:579px"><span class="drink-name">ROSSETTI ORANGE</span><span class="leader"></span><span class="volume">0,2L</span><span class="leader is-price"></span><span class="price">7,50</span></li>
    <li class="drink" style="top:623px"><span class="drink-name">ROSSETTI SODA</span><span class="leader"></span><span class="volume">0,2L</span><span class="leader is-price"></span><span class="price">7,00</span></li>
    <li class="drink" style="top:667px"><span class="drink-name is-tight">VARELLI BIANCO/ROSSO/EXTRA DRY</span><span class="leader"></span><span class="volume">5CL</span><span class="leader is-price"></span><span class="price">7,00</span></li>
    <li class="drink" style="top:711px"><span class="drink-name is-tight">DUVALLE &amp; FILS BRUT</span><span class="leader"></span><span class="volume">0,2L</span><span class="leader is-short"></span><span class="volume">25,00</span><span class="leader is-short"></span><span class="volume">0,75L</span><span class="leader is-price"></span><span class="price">85,00</span></li>
    <li class="drink" style="top:756px"><span class="drink-name is-tight">DUVALLE &amp; FILS ROSE</span><span class="leader"></span><span class="volume">0,2L</span><span class="leader is-short"></span><span class="volume">25,00</span><span class="leader is-short"></span><span class="volume">0,75L</span><span class="leader is-price"></span><span class="price">92,00</span></li>
    <li class="drink" style="top:800px"><span class="drink-name is-tight">RIESLING SEKT TROCKEN</span><span class="leader"></span><span class="volume">0,75L</span><span class="leader is-price"></span><span class="price">30,00</span></li>
    <li class="drink" style="top:844px"><span class="drink-name is-tight">RIESLING SEKT TROCKEN</span><span class="leader"></span><span class="volume">0,1L</span><span class="leader is-price"></span><span class="price">8,00</span></li>
    <li class="drink" style="top:888px"><span class="drink-name is-tight">VON STRELL RIESLING BRUT 2017</span><span class="leader"></span><span class="volume">0,75L</span><span class="leader is-price"></span><span class="price">45,00</span></li>
    <li class="drink" style="top:934px"><span class="drink-name" style="min-width:250px">MARNAY&amp;LISSE-CRÉMANT<br>AZUR BRUT VINTAGE LOIRE</span><span class="leader"></span><span class="volume">0,75L</span><span class="leader is-price"></span><span class="price">45,00</span></li>
    <li class="drink" style="top:1003px"><span class="drink-name" style="min-width:250px">MARNAY &amp; LISSE-CRÉMANT<br>ROSÉ BRUT EXCELLENCE LOIR</span><span class="leader"></span><span class="volume">0,75L</span><span class="leader is-price"></span><span class="price">45,00</span></li>
  </ul>
</main>
</body>
</html>
```